harborline slab pumping "just pump it"

I want very easy to understand cards that say everything we offer.
i want the company name/logo, phone number and email on the front of card.
i want the card to stand out, it can be red with black lettering.
on the back of the card i want it to list everything that we can do like a list
the motto is JUST PUMP IT.
the can be in the lower right corner of the back of the card

Target Market(s)

concrete contractors

Industry/Entity Type

Concrete

Contact Information for Business Card

back of the card
Owner:Marco Tellin
Phone:503)418-6093
Email: HSPumping@slabmail.example
address: 22816 se brindle ave Portland, OR 97236

Colors
ec1f27
000000
959595
5c5c5c
f04a50
ffffff
f37122

Requirements
Must have
• :we have years of experience in the world of concrete
• :our pumps can do up to 70 yards an hour
• :if you refer us to other contractors, will give you up to 10% off next pump job
• :don’t hesitate to call if you have any concrete related questions and to get a qoute
• Please put this on the front of the card, “just pump it” in the lower right corner

```html
<!DOCTYPE html>
<html lang="en">
<head>
<meta charset="utf-8">
<title>Harborline Slab Pumping – Business Cards</title>
<link rel="stylesheet" href="https://fonts.googleapis.com/css2?family=Montserrat:wght@400;600;700&family=Open+Sans:wght@400;600&display=swap">
<style>
  :root {
    --red: #ec1f27;
    --red-soft: #f04a50;
    --black: #000000;
    --charcoal: #1c1c1c;
    --grey: #959595;
    --grey-dark: #5c5c5c;
    --white: #ffffff;
    --paper: #f6f6f6;
    --backdrop: #e4e2de;
  }
  * { box-sizing: border-box; margin: 0; padding: 0; }
  html, body { width: 1200px; height: 942px; overflow: hidden; }
  body {
    background: var(--backdrop);
    font-family: "Open Sans", Arial, sans-serif;
    position: relative;
  }
  .card {
    position: absolute;
    left: 250px;
    width: 700px;
    height: 400px;
    overflow: hidden;
    box-shadow: 0 8px 24px rgba(0,0,0,.22);
  }

  /* Front */
  .card--front { top: 50px; background: linear-gradient(160deg, var(--white), var(--paper)); }
  .edge-band {
    position: absolute; top: 0; left: 0; right: 0; height: 50px; display: flex;
  }
  .edge-band__claim {
    flex: 0 0 420px; background: var(--charcoal); color: var(--white);
    font-size: 17px; display: flex; align-items: center; padding-left: 26px;
  }
  .edge-band__refer {
    flex: 1; background: linear-gradient(90deg, var(--red), var(--red-soft));
    color: var(--white); font-size: 17px; display: flex; align-items: center;
    justify-content: flex-end; padding-right: 26px;
    clip-path: polygon(22px 0, 100% 0, 100% 100%, 0 100%);
  }
  .brand { position: absolute; font-family: "Montserrat", Arial, sans-serif; }
  .brand--front { left: 40px; top: 120px; }
  .brand__name {
    display: flex; align-items: center; gap: 10px;
    color: var(--red); font-weight: 700; font-size: 30px; letter-spacing: 1px;
    white-space: nowrap;
  }
  .brand__dot { width: 28px; height: 28px; border-radius: 50%; background: var(--red); flex: 0 0 auto; }
  .brand__sub {
    margin-top: 4px; margin-left: 38px; color: var(--grey-dark);
    font-size: 12px; letter-spacing: 3px; font-weight: 400; white-space: nowrap;
  }
  .divider {
    position: absolute; left: 320px; top: 170px; width: 2px; height: 170px; background: var(--red);
  }
  .contact { position: absolute; left: 345px; top: 175px; width: 330px; }
  .contact__name {
    font-family: "Montserrat", Arial, sans-serif; font-size: 26px; color: var(--charcoal);
    font-weight: 400; letter-spacing: 1px; white-space: nowrap;
  }
  .contact__name strong { font-weight: 700; }
  .contact__role { color: var(--red); font-size: 16px; margin-top: 2px; }
  .contact__list { list-style: none; margin-top: 16px; }
  .contact__item {
    display: flex; align-items: center; gap: 10px; font-size: 16px; color: var(--charcoal);
    margin-bottom: 8px; white-space: nowrap;
  }
  .contact__item svg { flex: 0 0 auto; }

  /* Back */
  .card--back {
    top: 492px;
    background: radial-gradient(ellipse at 65% 45%, #3a3a3a 0%, #151515 60%, #050505 100%);
  }
  .brand--back { left: 50%; top: 110px; transform: translateX(-50%); }
  .brand--back .brand__name { font-size: 52px; gap: 14px; }
  .brand--back .brand__dot { width: 44px; height: 44px; }
  .brand--back .brand__sub { color: var(--white); font-size: 19px; letter-spacing: 5px; margin-left: 58px; }
  .motto {
    position: absolute; right: 60px; bottom: 120px;
    font-family: "Montserrat", Arial, sans-serif; color: var(--red-soft); font-size: 18px; letter-spacing: 2px;
  }
  .motto strong { font-weight: 700; }
  .services {
    position: absolute; left: 0; right: 0; bottom: 34px; text-align: center;
    color: var(--white); font-size: 18px; letter-spacing: .5px;
  }
  .services span { margin: 0 12px; }
</style>
</head>
<body>

<section class="card card--front" aria-label="Business card front">
  <div class="edge-band">
    <div class="edge-band__claim">Our pumps can do up to 70 yards an hour</div>
    <div class="edge-band__refer">Please refer us</div>
  </div>

  <div class="brand brand--front">
    <div class="brand__name"><span class="brand__dot"></span>HARBORLINE</div>
    <div class="brand__sub">SLAB PUMPING</div>
  </div>

  <div class="divider"></div>

  <div class="contact">
    <div class="contact__name">MARCO <strong>TELLIN</strong></div>
    <div class="contact__role">Owner</div>
    <ul class="contact__list">
      <li class="contact__item">
        <svg width="16" height="16" viewBox="0 0 24 24" aria-hidden="true"><path fill="#ec1f27" d="M6.6 10.8a15.1 15.1 0 0 0 6.6 6.6l2.2-2.2c.3-.3.7-.4 1-.2 1.1.4 2.3.6 3.6.6.6 0 1 .4 1 1V20c0 .6-.4 1-1 1A17 17 0 0 1 3 4c0-.6.4-1 1-1h3.5c.6 0 1 .4 1 1 0 1.3.2 2.5.6 3.6.1.3 0 .7-.2 1z"/></svg>
        (503)418-6093
      </li>
      <li class="contact__item">
        <svg width="16" height="16" viewBox="0 0 24 24" aria-hidden="true"><rect x="2" y="5" width="20" height="14" fill="#ec1f27"/><path d="M2 5l10 8 10-8" fill="none" stroke="#fff" stroke-width="1.8"/></svg>
        HSPumping@slabmail.example
      </li>
    </ul>
  </div>
</section>

<section class="card card--back" aria-label="Business card back">
  <div class="brand brand--back">
    <div class="brand__name"><span class="brand__dot"></span>HARBORLINE</div>
    <div class="brand__sub">SLAB PUMPING</div>
  </div>
  <div class="motto">JUST <strong>PUMP IT</strong></div>
  <div class="services">Our service 1<span>|</span>Our Service 2<span>|</span>Our Service 3</div>
</section>

</body>
</html>
```